Hollowbrook Print and Ink Business

Hi, I need template designs for stationary as listed below using my Logo as per attached file;
1) Business Card (double sided)
2) Letterhead
3) With Compliments Slip
4) Return Address Label (Stickers)

```html
<!DOCTYPE html>
<html lang="en">
<head>
<meta charset="utf-8">
<title>Hollowbrook Print and Ink – Letterhead</title>
<link rel="stylesheet" href="https://fonts.googleapis.com/css2?family=Roboto+Condensed:wght@400;700&display=swap">
<style>
  :root {
    --paper: #ffffff;
    --ink: #2b2b2b;
    --brand-magenta: #c2258c;
    --rule-purple: #8b3f92;
    --rule-green: #3f9a44;
  }
  html, body {
    margin: 0;
    padding: 0;
    overflow: hidden;
    background: var(--paper);
  }
  .letterhead {
    position: relative;
    width: 849px;
    height: 1200px;
    background: var(--paper);
    font-family: "Roboto Condensed", "Arial Narrow", sans-serif;
    color: var(--ink);
    overflow: hidden;
  }
  .rule {
    position: absolute;
    width: 2px;
    bottom: 0;
  }
  .rule--outer { left: 712px; top: 0; background: var(--rule-purple); }
  .rule--middle { left: 718px; top: 128px; background: var(--rule-green); }
  .rule--inner { left: 724px; top: 276px; background: var(--rule-green); }

  .brand {
    position: absolute;
    left: 728px;
    top: 44px;
    width: 110px;
    display: flex;
    align-items: flex-start;
    gap: 6px;
  }
  .brand__dot {
    flex: none;
    width: 12px;
    height: 12px;
    margin-top: 3px;
    border-radius: 50%;
    background: var(--brand-magenta);
  }
  .brand__name {
    margin: 0;
    font-size: 16px;
    font-weight: 700;
    line-height: 1.05;
    color: var(--brand-magenta);
  }

  .contact {
    position: absolute;
    left: 727px;
    top: 150px;
    margin: 0;
    font-style: normal;
    font-size: 12.5px;
    line-height: 15.8px;
    letter-spacing: -0.1px;
  }
  .contact__line { display: block; white-space: nowrap; }
  .contact__label {
    font-weight: 700;
    color: var(--brand-magenta);
    display: inline-block;
    min-width: 22px;
  }
  .contact__label--tight { min-width: 14px; }

  .abn {
    position: absolute;
    left: 308px;
    top: 1164px;
    margin: 0;
    font-size: 12px;
    letter-spacing: -0.1px;
  }
</style>
</head>
<body>
  <main class="letterhead">
    <div class="rule rule--outer"></div>
    <div class="rule rule--middle"></div>
    <div class="rule rule--inner"></div>

    <header class="brand">
      <span class="brand__dot"></span>
      <p class="brand__name">Hollowbrook Print and Ink</p>
    </header>

    <address class="contact">
      <span class="contact__line">111 Name Street</span>
      <span class="contact__line">City&nbsp; State&nbsp; Postcode</span>
      <span class="contact__line"><span class="contact__label">P:</span>(xx) xxxx xxxx</span>
      <span class="contact__line"><span class="contact__label">F:</span>(xx) xxxx xxxx</span>
      <span class="contact__line"><span class="contact__label">M:</span>xxxx xxx xxx</span>
      <span class="contact__line"><span class="contact__label contact__label--tight">E:</span>studio@xxxx.com</span>
      <span class="contact__line">www.xxxx.com</span>
    </address>

    <p class="abn">ABN xx xxx xxx xxx</p>
  </main>
</body>
</html>
```